Cover für ein Taschenbuch zum Thema Ruhestand gesucht!
Zielgruppe
Unsere Zielgruppe sind Senioren, bzw. Menschen im Alter 50+. Es handelt sich bei dem Buch um einen Ratgeber zum Thema 'Ruhestand'. Allerdings wird das Buch ebenso von einer jüngeren Zielgruppe gekauft, da der Ratgeber auch gerne an Eltern oder Großeltern verschenkt wird.
Aufgabenstellung
siehe Dateiupload
Format: 5,25' x 8'

```html
<!DOCTYPE html>
<html lang="de">
<head>
<meta charset="utf-8">
<title>Neue Freiheit – Buchcover</title>
<link rel="stylesheet" href="https://fonts.googleapis.com/css2?family=Cinzel:wght@600;700&family=Lora:ital,wght@0,400;1,700&display=swap">
<style>
  :root {
    --page-bg: #ececec;
    --sky-top: #1f93c9;
    --sky-mid: #5ab6dd;
    --haze: #f3ecd9;
    --sun: #ffd27a;
    --sunset: #f29a2e;
    --sand: #d8621d;
    --sand-deep: #b84a17;
    --title-white: #ffffff;
    --label-blue: #2a8dc2;
    --tagline-blue: #1f6f9c;
  }
  html, body {
    margin: 0;
    padding: 0;
    width: 1200px;
    height: 3033px;
    overflow: hidden;
    background: var(--page-bg);
  }
  .canvas {
    position: relative;
    width: 1200px;
    height: 3033px;
  }
  .book-cover {
    position: absolute;
    left: 200px;
    top: 907px;
    width: 800px;
    height: 1219px;
    overflow: hidden;
    box-shadow: 0 20px 50px rgba(0,0,0,0.18);
  }
  .cover-photo {
    position: absolute;
    inset: 0;
    width: 100%;
    height: 100%;
  }
  .cover-text {
    position: absolute;
    inset: 0;
    text-align: center;
  }
  .title-small {
    position: absolute;
    top: 62px;
    left: 0;
    right: 0;
    margin: 0;
    font-family: "Cinzel", serif;
    font-weight: 700;
    font-size: 92px;
    line-height: 1;
    color: var(--title-white);
    text-shadow: 0 2px 6px rgba(0,0,0,0.25);
  }
  .title-main {
    position: absolute;
    top: 160px;
    left: 0;
    right: 0;
    margin: 0;
    font-family: "Cinzel", serif;
    font-weight: 700;
    font-size: 108px;
    line-height: 1;
    letter-spacing: 1px;
    color: var(--title-white);
    text-shadow: 0 2px 6px rgba(0,0,0,0.25);
  }
  .subtitle {
    position: absolute;
    top: 276px;
    left: 0;
    right: 0;
    margin: 0;
    font-family: "Cinzel", serif;
    font-weight: 600;
    font-size: 29px;
    letter-spacing: 1px;
    color: var(--title-white);
  }
  .author-label {
    position: absolute;
    top: 362px;
    left: 252px;
    width: 296px;
    height: 66px;
    background: var(--label-blue);
    display: flex;
    align-items: center;
    justify-content: center;
    font-family: "Lora", serif;
    font-style: italic;
    font-weight: 700;
    font-size: 31px;
    color: var(--title-white);
  }
  .tagline {
    position: absolute;
    top: 505px;
    left: 130px;
    right: 130px;
    margin: 0;
    font-family: "Lora", serif;
    font-size: 26px;
    line-height: 1.28;
    color: var(--tagline-blue);
  }
</style>
</head>
<body>
<div class="canvas">
  <div class="book-cover">
    <svg class="cover-photo" viewBox="0 0 800 1219" preserveAspectRatio="none" role="img" aria-label="Foto: älteres Paar in Liegestühlen am Strand bei Sonnenuntergang, Hand in Hand">
      <defs>
        <linearGradient id="sky-to-sand" x1="0" y1="0" x2="0" y2="1">
          <stop offset="0" stop-color="var(--sky-top)"/>
          <stop offset="0.3" stop-color="var(--sky-mid)"/>
          <stop offset="0.6" stop-color="var(--haze)"/>
          <stop offset="0.78" stop-color="var(--sunset)"/>
          <stop offset="0.9" stop-color="var(--sand)"/>
          <stop offset="1" stop-color="var(--sand-deep)"/>
        </linearGradient>
        <radialGradient id="sun-glow" cx="0.44" cy="0.8" r="0.35">
          <stop offset="0" stop-color="var(--sun)" stop-opacity="0.9"/>
          <stop offset="1" stop-color="var(--sun)" stop-opacity="0"/>
        </radialGradient>
      </defs>
      <rect width="800" height="1219" fill="url(#sky-to-sand)"/>
      <rect width="800" height="1219" fill="url(#sun-glow)"/>
    </svg>
    <div class="cover-text">
      <h1 class="title-small">NEUE</h1>
      <h1 class="title-main">FREIHEIT</h1>
      <p class="subtitle">JETZT BEGINNT DIE SCHÖNSTE ZEIT!</p>
      <div class="author-label">Konrad Albers</div>
      <p class="tagline">Praktische Ideen und Ratschläge, mit denen Sie Ihre freien Jahre voller Freude gestalten können</p>
    </div>
  </div>
</div>
</body>
</html>
```